Graphic Design for a Info Card

We would like a graphic design for an info card . We would like the colours to correspond to our logo , you can add in the colours navy blue or yellow if you would like. We would like it to have the following information. We want something that really pops. We would like the size to be 4 1/2 x 6 .

ATTENTION!! Delivery Promo! Order from us on the @hopplemeals app or @marlinrunner app on FRIDAYS and receive a FREE Sample of our one of our meal prep meals in your bag!
DID YOU KNOW?! Meal Prep is another great service that we offer. Saving you time, promoting your health, and best of all providing a delicious lunch . You can find more info on our website www.brivoranpantry.example . All orders are available for delivery or pickup!

```html
<!DOCTYPE html>
<html lang="en">
<head>
<meta charset="UTF-8">
<title>Brivoran Delivery Promo Card</title>
<link rel="stylesheet" href="https://fonts.googleapis.com/css2?family=Poppins:ital,wght@0,500;0,600;0,700;1,600&display=swap">
<style>
  :root {
    --navy: #191a45;
    --navy-deep: #13143a;
    --green: #8cc63f;
    --white: #ffffff;
    --page: #e9e7e2;
    --ink: #191a45;
  }
  * { margin: 0; padding: 0; box-sizing: border-box; }
  html, body { width: 1200px; height: 1200px; overflow: hidden; background: var(--page); }
  body { font-family: "Poppins", sans-serif; position: relative; }

  .card {
    position: absolute; left: 210px; top: 80px;
    width: 780px; height: 1040px;
    background: var(--navy);
    border-radius: 32px;
    overflow: hidden;
    color: var(--white);
  }
  .card > * { position: absolute; }

  .swirl { left: 0; top: 0; width: 780px; height: 1040px; }

  .photo { border-radius: 50%; }
  .photo-salmon {
    left: 383px; top: 58px; width: 496px; height: 496px;
    background: radial-gradient(circle at 45% 30%, #d9a26a 0%, #b8773f 25%, #6b8a3a 55%, #3d6b2a 80%, #2a4a1f 100%);
  }
  .photo-chicken {
    left: 594px; top: 603px; width: 272px; height: 272px;
    background: radial-gradient(circle at 35% 45%, #e6a15a 0%, #d2843f 35%, #8aa349 65%, #4f7a2f 100%);
    border: 4px solid var(--navy);
  }
  .photo-plate {
    left: 409px; top: 516px; width: 210px; height: 210px;
    background: radial-gradient(circle, #7a5a3e 0%, #9a6a48 40%, #c9a889 62%, #f1efe9 66%, #f7f6f2 100%);
    border: 4px solid var(--navy);
  }

  .brand { left: 50px; top: 28px; }
  .brand-name {
    font-weight: 700; font-size: 74px; line-height: 1;
    letter-spacing: 1px; color: var(--green);
  }
  .brand-tag {
    margin-top: 12px; font-weight: 700; font-size: 25px; color: var(--green);
    letter-spacing: 0.3px; white-space: nowrap;
  }

  .attention {
    left: 50px; top: 170px;
    font-weight: 700; font-size: 54px; line-height: 1.1; color: var(--green);
  }

  .band {
    left: 0; height: 60px; display: flex; align-items: center;
    padding-left: 50px; font-weight: 700; font-size: 37px; color: var(--ink);
    white-space: nowrap;
  }
  .band-promo { top: 256px; width: 470px; background: var(--white); }
  .band-know { top: 640px; width: 408px; background: var(--green); padding-left: 52px; }

  .order {
    left: 52px; top: 334px;
    font-weight: 600; font-size: 27px; line-height: 37px;
  }
  .handle { color: var(--green); }

  .sample {
    left: 52px; top: 506px;
    font-weight: 500; font-size: 20px; line-height: 31px;
  }

  .about {
    left: 52px; top: 712px; width: 430px;
    font-weight: 500; font-size: 17px; line-height: 26px;
  }

  .more {
    left: 52px; top: 790px;
    font-weight: 500; font-size: 23px; line-height: 34px;
  }
  .website { display: block; font-weight: 700; font-size: 25px; color: var(--green); }

  .service {
    left: 170px; top: 908px; width: 450px; text-align: center;
    font-weight: 600; font-style: italic; font-size: 25px; line-height: 38px;
  }

  .footer-wave { left: 0; top: 0; width: 780px; height: 1040px; }
</style>
</head>
<body>
  <main class="card">
    <svg class="swirl" viewBox="0 0 780 1040" aria-hidden="true">
      <path d="M0 760 C150 700 260 820 430 780 C560 750 650 640 780 620 L780 1040 L0 1040 Z" fill="var(--navy-deep)" opacity="0.45"/>
      <path d="M600 0 C520 60 480 130 470 200 L780 200 L780 0 Z" fill="var(--navy-deep)" opacity="0.35"/>
    </svg>

    <div class="photo photo-salmon" role="img" aria-label="Photo of a glazed salmon fillet over roasted vegetables and greens"></div>
    <div class="photo photo-chicken" role="img" aria-label="Photo of sliced grilled chicken on a fresh salad"></div>
    <div class="photo photo-plate" role="img" aria-label="Photo of a plated ground beef bowl topped with sauces and onions"></div>

    <header class="brand">
      <div class="brand-name">BRIVORAN</div>
      <div class="brand-tag">HEALTHY KITCHEN &nbsp;|&nbsp; MEAL PREP</div>
    </header>

    <h1 class="attention">ATTENTION!!</h1>

    <h2 class="band band-promo">DELIVERY PROMO!</h2>

    <p class="order">
      Order from us on the<br>
      <span class="handle">@hopplemeals</span> app<br>
      or <span class="handle">@marlinrunner</span> app<br>
      on FRIDAYS
    </p>

    <p class="sample">
      and receive a FREE Sample of our<br>
      one of our meal prep meals<br>
      in your bag!
    </p>

    <h2 class="band band-know">DID YOU KNOW?!</h2>

    <p class="about">
      Meal Prep is another great service that we offer. Saving you time, promoting your health, and best of all providing a delicious lunch .
    </p>

    <p class="more">
      You can find more info on our website
      <span class="website">www.brivoranpantry.example</span>
    </p>

    <svg class="footer-wave" viewBox="0 0 780 1040" aria-hidden="true">
      <path d="M0 985 C180 1015 420 1000 560 975 C660 955 730 930 780 900 L780 1040 L0 1040 Z" fill="var(--green)"/>
      <path d="M700 960 C690 920 720 880 780 870 L780 885 C740 895 715 925 712 955 Z" fill="var(--white)"/>
    </svg>

    <p class="service">All orders are available for<br>delivery or pickup!</p>
  </main>
</body>
</html>
```